Marlowe's Classic Dressing

We are looking for a new label as we switch or glass bottle from a traditional bottle to a round bottle. We want to create a newer/ more appealing logo, while still maintaining some of our old label features to ensure that the brand awareness is not lost. We like the coloring of the blue and white, but feel free to play around with other colors in the design.
We are looking to add product features to our label such as "Gluten-Free", "Original Recipe From 1957" "Family Owned". With this being an older company we would like to keep the traditional feel of our label with some added modern touches.
We are not married to the greek logo/ building but would love some designs with and without it.
WE ARE LOOKING FOR A ROUND LABEL. The pictures provided below are of the old bottle.
There is a picture of the ringneck bottle below. The size of the label is 4.00 x 7.00.

```html
<!DOCTYPE html>
<html lang="en">
<head>
<meta charset="utf-8">
<title>Marlowe's Classic Dressing – Round Label</title>
<link rel="stylesheet" href="https://fonts.googleapis.com/css2?family=Cinzel:wght@400;600;700&display=swap">
<style>
  :root {
    --label-blue: #1a62ae;
    --accent-orange: #e06c28;
    --paper: #ffffff;
  }
  html, body {
    margin: 0;
    padding: 0;
    width: 1038px;
    height: 1200px;
    overflow: hidden;
    background: var(--paper);
  }
  .canvas {
    width: 1038px;
    height: 1200px;
    display: flex;
    align-items: center;
    justify-content: center;
  }
  .round-label {
    width: 1000px;
    height: 1000px;
    display: block;
  }
  .label-text {
    font-family: "Cinzel", serif;
  }
  .brand-name { fill: var(--accent-orange); font-weight: 700; }
  .product-title {
    fill: var(--label-blue);
    stroke: var(--paper);
    stroke-width: 5;
    paint-order: stroke;
    font-weight: 700;
  }
  .product-subtitle { fill: var(--label-blue); font-weight: 600; }
  .tagline { fill: var(--label-blue); font-weight: 600; letter-spacing: 7px; }
  .year { fill: var(--accent-orange); font-weight: 400; }
  .arc-claim { fill: var(--label-blue); font-weight: 600; letter-spacing: 22px; }
  .volume { fill: var(--paper); font-weight: 600; }
  .badge-text { fill: var(--paper); font-weight: 600; }
  .blue-fill { fill: var(--label-blue); }
  .white-fill { fill: var(--paper); }
  .key-border { fill: none; stroke: var(--label-blue); stroke-width: 32; }
  .rule { stroke: var(--accent-orange); stroke-width: 2.5; }
</style>
</head>
<body>
<main class="canvas">
  <svg class="round-label" viewBox="621 248 1034 1034" xmlns="http://www.w3.org/2000/svg" aria-label="Marlowe's Greek Dressing round label">
    <defs>
      <clipPath id="inner-disc">
        <circle cx="1138" cy="765" r="482"/>
      </clipPath>
      <path id="top-arc" d="M 698 765 A 440 440 0 0 1 1578 765"/>
      <path id="bottom-arc" d="M 690 765 A 448 448 0 0 0 1586 765"/>
    </defs>

    <!-- outer ring -->
    <circle class="blue-fill" cx="1138" cy="765" r="517"/>
    <circle class="white-fill" cx="1138" cy="765" r="494"/>

    <!-- bottom band -->
    <rect class="blue-fill" x="600" y="1100" width="1080" height="200" clip-path="url(#inner-disc)"/>

    <!-- key-pattern border arcs -->
    <path class="key-border" role="img" aria-label="Greek key border pattern" d="M 705 626 A 455 455 0 0 1 853 410"/>
    <path class="key-border" role="img" aria-label="Greek key border pattern" d="M 1423 410 A 455 455 0 0 1 1571 626"/>
    <path class="key-border" role="img" aria-label="Greek key border pattern" d="M 688 832 A 455 455 0 0 0 823 1093"/>
    <path class="key-border" role="img" aria-label="Greek key border pattern" d="M 1453 1093 A 455 455 0 0 0 1588 832"/>

    <!-- arc claim -->
    <text class="label-text arc-claim" font-size="34">
      <textPath href="#top-arc" startOffset="50%" text-anchor="middle">FAMILY OWNED</textPath>
    </text>

    <!-- brand name -->
    <text class="label-text brand-name" x="1138" y="618" font-size="112" text-anchor="middle" textLength="470" lengthAdjust="spacingAndGlyphs">Marlowe's</text>

    <!-- title band -->
    <rect class="blue-fill" x="655" y="630" width="966" height="167"/>
    <text class="label-text product-title" x="1138" y="797" font-size="232" text-anchor="middle" textLength="790" lengthAdjust="spacingAndGlyphs">GREEK</text>

    <text class="label-text product-subtitle" x="1138" y="887" font-size="98" text-anchor="middle" textLength="530" lengthAdjust="spacingAndGlyphs">DRESSING</text>

    <text class="label-text tagline" x="1138" y="945" font-size="20" text-anchor="middle" textLength="405" lengthAdjust="spacing">ORIGINAL RECIPE FROM</text>

    <!-- year with rules -->
    <g class="year-lockup">
      <line class="rule" x1="975" y1="977" x2="1080" y2="977"/>
      <line class="rule" x1="1010" y1="970" x2="1080" y2="970"/>
      <line class="rule" x1="1010" y1="984" x2="1080" y2="984"/>
      <line class="rule" x1="1196" y1="977" x2="1301" y2="977"/>
      <line class="rule" x1="1196" y1="970" x2="1266" y2="970"/>
      <line class="rule" x1="1196" y1="984" x2="1266" y2="984"/>
      <text class="label-text year" x="1138" y="995" font-size="50" text-anchor="middle">1957</text>
    </g>

    <!-- gluten free badge -->
    <g class="claim-badge">
      <circle class="white-fill" cx="1138" cy="1108" r="86"/>
      <circle class="blue-fill" cx="1138" cy="1108" r="78"/>
      <text class="label-text badge-text" x="1138" y="1108" font-size="21" text-anchor="middle">GLUTEN</text>
      <text class="label-text badge-text" x="1138" y="1132" font-size="21" text-anchor="middle">FREE</text>
    </g>

    <!-- volume -->
    <text class="label-text volume" font-size="26">
      <textPath href="#bottom-arc" startOffset="50%" text-anchor="middle">8FL. OZ. (237ML)</textPath>
    </text>
  </svg>
</main>
</body>
</html>
```